Brochure design - Velora

We offer integrated software solutions for independent and chain hotel service businesses. Such businesses would include any independent hotels with 100+ bedrooms or chains like Bexworth, Tolvina etc with 3-5 outlets. Our software is configured for the needs of each type of business and spans both guest facing and back office functions.

The core benefits our solution offers is that it is -
1. integrated to cater to all the service issues of the hotels, interdepartmental communications and incident reporting in the hotels.
2. functionally powerful and compare well with the best available internationally.
3. Developed using the latest in software technology ... for example, escalation to managers or delayed service delivery via SMS or emial gateway.

The market is a mature market with many competitors. A few very well established with huge track record. We have a track record internationally but are new to the UK market. This brochure is targeted at the UK market. The target market is jaded with the number of options available. We will focus on independent hotels with a hope that the product would excite them as the competitors are more expensive for this market. But we also want to mention that we can also serve the big chains equally to convey the versatility of our solution and for the other businesses that we may be able to attract.

We are hoping that the brochure will stand-out from the crowd and will compel the market to browse through what we do.

Some key competitors in the UK include -
http://www.quarnex.example/products/rubelo/
http://www.vandisa.example/en/morvel/
http://www.glentra.example/gtx-e-reach-and-m-reach/

We have a company and sample product brochure we made (both attached). We have also developed a web site (see www.harbenwise.example). The brochure design need not conform to the web site, if (and only if) you can come up with a really attention seeking design (we could consider redesign of the web site).

The content of the brochure will largely conform to the sample brochure submitted because we have carefully taken the content out for the sample brochure.

new brief updated for the design of 1 brochure which is needed

Target Market(s)

UK Hotels with more than 100 bedrooms which would include independent and chain hotels with 3-5 outlets.

Industry/Entity Type

Communications

Font styles to use
Sans Serif

Colors
f04a50
faa54b
f8a44a
ec1f27
faee3f
fece3e
cbcbcb
e6e6e6

Requirements
Must have
• - Flowchart enhanced
- hotel services pictures
Nice to have
• Nice to have a design that relates the solution to UK either in terms of colors or visuals. the design should be elegant and professional in appearance but playful and not very serious.

```html
<!DOCTYPE html>
<html lang="en">
<head>
<meta charset="utf-8">
<title>Management Analysis</title>
<link rel="stylesheet" href="https://fonts.googleapis.com/css2?family=Josefin+Sans:wght@300;400;600&family=Open+Sans:wght@600&display=swap">
<style>
  :root {
    --red: #ec1f27;
    --coral: #f04a50;
    --orange: #faa54b;
    --orange-deep: #f8a44a;
    --bg: #c8c8c8;
    --panel: #d6d6d6;
    --arrow: #6f6f6f;
    --ink: #1c1c1c;
  }
  * { margin: 0; padding: 0; box-sizing: border-box; }
  html, body { width: 1200px; height: 900px; overflow: hidden; }
  body { background: var(--bg); font-family: "Josefin Sans", sans-serif; color: var(--ink); }
  .page { position: relative; width: 1200px; height: 900px; overflow: hidden;
    background: radial-gradient(ellipse at 45% 50%, #d2d2d2 0%, var(--bg) 75%); }
  .edge-band { position: absolute; left: 0; top: 0; }
  .title { position: absolute; left: 120px; top: 24px; font-weight: 400; font-size: 53px;
    font-variant: small-caps; letter-spacing: 2px; white-space: nowrap; }
  .info-panel { position: absolute; left: 946px; top: 44px; width: 212px; height: 820px;
    background: linear-gradient(to right, #cfcfcf, var(--panel) 15%, var(--panel) 85%, #cdcdcd);
    box-shadow: -10px 0 18px rgba(0,0,0,0.12); padding: 32px 14px 0 0; text-align: right;
    font-family: "Open Sans", sans-serif; font-weight: 600; font-size: 14px; line-height: 20px; color: var(--red); }
  .info-panel p { margin-bottom: 20px; white-space: nowrap; }
  .cycle { position: absolute; left: 0; top: 0; }
  .label { position: absolute; font-size: 13px; line-height: 17px; font-weight: 600; white-space: nowrap; }
  .label.center { text-align: center; transform: translateX(-50%); }
  .hub { position: absolute; left: 512px; top: 414px; transform: translateX(-50%);
    text-align: center; font-weight: 400; font-size: 20px; line-height: 26px; white-space: nowrap; }
</style>
</head>
<body>
<div class="page">
  <svg class="edge-band" width="230" height="900" viewBox="0 0 230 900" aria-hidden="true">
    <defs>
      <linearGradient id="bandFill" x1="0" y1="0" x2="1" y2="0">
        <stop offset="0" stop-color="#f7a94d"/>
        <stop offset="0.55" stop-color="var(--coral)"/>
        <stop offset="1" stop-color="var(--red)"/>
      </linearGradient>
    </defs>
    <path d="M0,0 H96 C70,160 118,300 104,450 C92,610 150,760 176,900 H0 Z" fill="url(#bandFill)"/>
    <path d="M96,0 C70,160 118,300 104,450 C92,610 150,760 176,900" fill="none" stroke="#f5d2c4" stroke-width="2" opacity="0.7"/>
    <path d="M0,0 H40 C20,200 60,380 40,560 C30,700 60,820 70,900 H0 Z" fill="var(--orange)" opacity="0.55"/>
  </svg>

  <h1 class="title">Management Analysis</h1>

  <svg class="cycle" width="940" height="900" viewBox="0 0 940 900" aria-hidden="true">
    <defs>
      <marker id="head" viewBox="0 0 10 10" refX="6" refY="5" markerWidth="4" markerHeight="4" orient="auto">
        <path d="M0,0 L10,5 L0,10 Z" fill="var(--arrow)"/>
      </marker>
    </defs>
    <g fill="none" stroke="var(--arrow)" stroke-width="5" marker-end="url(#head)">
      <path d="M360,222 Q402,196 450,188"/>
      <path d="M554,190 Q604,200 644,226"/>
      <path d="M720,288 Q750,322 766,362"/>
      <path d="M790,474 Q790,520 776,560"/>
      <path d="M720,654 Q684,698 640,724"/>
      <path d="M552,754 Q504,758 460,754"/>
      <path d="M360,718 Q324,700 298,674"/>
      <path d="M240,564 Q228,516 232,472"/>
      <path d="M240,366 Q256,324 284,290"/>
    </g>

    <g fill="none" stroke="var(--red)" stroke-width="6" stroke-linecap="round" stroke-linejoin="round">
      <!-- call escalation: hung-up handset with rising arrow -->
      <path d="M470,216 L476,196 Q504,180 532,196 L538,216 L524,222 L518,206 Q504,200 490,206 L484,222 Z" stroke-width="5"/>
      <path d="M474,152 L498,174 L530,144"/>
      <path d="M516,142 H532 V158"/>
      <!-- staff performance -->
      <path d="M652,220 V282 H716"/>
      <rect x="662" y="260" width="10" height="16"/><rect x="680" y="248" width="10" height="28"/><rect x="698" y="226" width="10" height="50"/>
      <!-- response time -->
      <circle cx="780" cy="414" r="34"/>
      <path d="M780,390 V414 H800"/>
      <!-- tasks by time -->
      <rect x="726" y="582" width="44" height="58" rx="3"/>
      <path d="M738,600 H758 M738,612 H758 M738,624 H750"/>
      <circle cx="768" cy="632" r="13" fill="var(--bg)"/><path d="M768,625 V632 H774" stroke-width="3"/>
      <!-- tasks by location -->
      <rect x="576" y="712" width="44" height="58" rx="3"/>
      <path d="M588,730 H608 M588,742 H608"/>
      <circle cx="618" cy="762" r="13" fill="var(--bg)"/><rect x="613" y="755" width="10" height="14" stroke-width="3"/>
      <!-- call frequency -->
      <path d="M382,702 Q374,712 384,730 Q398,752 418,756 Q428,750 426,742 L412,732 L404,738 Q394,730 390,720 L396,712 L388,698 Z" fill="var(--red)" stroke-width="3"/>
      <path d="M408,702 Q418,704 420,714 M410,690 Q428,694 432,712" stroke-width="3"/>
      <!-- department efficiency -->
      <path d="M236,600 A34,34 0 1 1 262,650"/>
      <path d="M268,598 V618 H282" stroke-width="4"/>
      <text x="248" y="646" font-family="Open Sans, sans-serif" font-size="38" font-weight="600" fill="var(--red)" stroke="none" text-anchor="middle">$</text>
      <!-- top tasks -->
      <rect x="204" y="388" width="46" height="60" rx="3"/>
      <path d="M216,404 H238 M216,416 H238 M216,428 H230"/>
      <circle cx="250" cy="444" r="14" fill="var(--bg)"/><path d="M250,436 V446 M250,451 V452" stroke-width="3"/>
      <!-- recurring tasks -->
      <path d="M286,228 A28,28 0 0 1 330,214"/>
      <path d="M338,252 A28,28 0 0 1 294,266"/>
      <path d="M322,204 L334,214 L320,222" stroke-width="5"/>
      <path d="M302,276 L290,266 L304,258" stroke-width="5"/>
    </g>
  </svg>

  <div class="label center" style="left:504px; top:106px;">Call<br>Escalation</div>
  <div class="label" style="left:736px; top:182px;">Staff<br>Performance<br>Report</div>
  <div class="label center" style="left:854px; top:392px;">Response<br>Time<br>Analysis</div>
  <div class="label" style="left:790px; top:612px;">Tasks by<br>Time, Date<br>&amp; Department</div>
  <div class="label" style="left:648px; top:768px;">Tasks by<br>Location<br>or Room</div>
  <div class="label center" style="left:390px; top:778px;">Call<br>Frequency</div>
  <div class="label" style="left:140px; top:628px;">Department<br>Efficiency</div>
  <div class="label" style="left:156px; top:402px;">Top<br>Tasks</div>
  <div class="label" style="left:216px; top:204px;">Recurring<br>Tasks</div>

  <p class="hub">Analyse Reports Using Velora<br>Enhanced Reporting System to<br>Identify Areas of Concern and<br>Factors of Process Improvement</p>

  <aside class="info-panel">
    <p>The system<br>produces valuable<br>intelligence for<br>management decision<br>making.</p>
    <p>The system reports<br>on incident trends by<br>service department,<br>incident type, and<br>location.</p>
    <p>Reports are also<br>available on departmental<br>and employee efficiency.</p>
    <p>The most important<br>feature is that it<br>produces a customer<br>satisfaction scorecard.</p>
  </aside>
</div>
</body>
</html>
```